Restaurant DIGITAL menu design- menu items name and description typed in already

Menu design for vietnamese sandwich restaurant menu board. Design will be used in 6 feet tall by 4 feet wide format on four 4k tv mounted VERTICALLY. Main colours of design yellow, white, black. Design should be FUN AND CASUAL.

Target Market(s)

Young professionals in 30-40s age group

Requirements
Must have
• Please note that this is FOUR 4K tv mounted VERTICALLY. Two on top, two on bottom VERTICALLY. All horizontal design will NOT be considered as winner.

Please use menu information in "MAIN FILE" for design, no generic or incorrect information.

No stock photos, free or pay
Link for more images

https://www.filvarenstash.example/sh/kq3r8tzmpa2w47x/BBFR_7LNqTw4hxjj9uWMPZbc?dl=0
Should not have
• HORIZONTAL DESIGN WILL NOT BE CONSIDERED.
No Stock photos.

```html
<!DOCTYPE html>
<html lang="en">
<head>
<meta charset="utf-8">
<title>Fresh Juices Menu</title>
<link href="https://fonts.googleapis.com/css2?family=Arvo&family=Mulish:wght@400;500&display=swap" rel="stylesheet">
<style>
  :root {
    --yellow: #f4ab13;
    --black: #000000;
    --white: #ffffff;
  }
  * { margin: 0; padding: 0; box-sizing: border-box; }
  html, body { width: 796px; height: 1200px; overflow: hidden; background: var(--yellow); }
  .menu {
    position: relative;
    width: 796px;
    height: 1200px;
    background: var(--yellow);
    font-family: "Mulish", sans-serif;
  }
  .section-band {
    position: absolute;
    left: 1px;
    right: 0;
    height: 78px;
    background: var(--black);
  }
  .section-band--juices { top: 84px; }
  .section-band--boost { top: 579px; }
  .section-title {
    position: absolute;
    top: 18px;
    font-family: "Arvo", serif;
    font-weight: 400;
    font-size: 34px;
    line-height: 1.2;
    color: var(--yellow);
    letter-spacing: 0.5px;
  }
  .section-band--juices .section-title { left: 76px; }
  .section-band--boost .section-title { left: 81px; }
  .item {
    position: absolute;
    left: 76px;
    width: 620px;
  }
  .item-name {
    font-size: 19px;
    font-weight: 400;
    line-height: 22px;
    color: var(--white);
    text-transform: uppercase;
  }
  .item-name .subtitle { text-transform: none; }
  .item-desc {
    font-size: 15.5px;
    font-weight: 400;
    line-height: 20px;
    color: var(--black);
  }
  .item-price {
    position: absolute;
    right: 0;
    bottom: 0;
    font-size: 15.5px;
    line-height: 20px;
    color: var(--black);
  }
</style>
</head>
<body>
<main class="menu">
  <header class="section-band section-band--juices">
    <h2 class="section-title">FRESH JUICES</h2>
  </header>

  <div class="item" style="top:200px">
    <p class="item-name">Good Morning: <span class="subtitle">An A.M. Juice</span></p>
    <p class="item-desc">apple | pear | carrot |lemon | orange</p>
    <span class="item-price">6</span>
  </div>
  <div class="item" style="top:263px">
    <p class="item-name">Green Goddess</p>
    <p class="item-desc">celery | cucumber | green apple | pear | lemon</p>
    <span class="item-price">6</span>
  </div>
  <div class="item" style="top:326px">
    <p class="item-name">Revitalize</p>
    <p class="item-desc">apple | carrot | lemon | ginger</p>
    <span class="item-price">6</span>
  </div>
  <div class="item" style="top:389px">
    <p class="item-name">Power-Up</p>
    <p class="item-desc">orange | lemon | ginger | apple</p>
    <span class="item-price">6</span>
  </div>
  <div class="item" style="top:452px">
    <p class="item-name">Sunna Signature</p>
    <p class="item-desc">Mango | green papaya | pineapple | lemon | orange</p>
    <span class="item-price">6</span>
  </div>

  <header class="section-band section-band--boost">
    <h2 class="section-title">JUICE BOOST</h2>
  </header>

  <div class="item" style="top:701px; width:613px">
    <p class="item-name">Superseed Blend (With Coconut)</p>
    <p class="item-desc">A boost of ground flax, chia and hemp seed</p>
    <span class="item-price">0.75</span>
  </div>
  <div class="item" style="top:767px; width:614px">
    <p class="item-name">Flaxseed With Mixed Berries</p>
    <p class="item-desc">A boost of ground flax, chia and hemp seed.</p>
    <span class="item-price">0.50</span>
  </div>
</main>
</body>
</html>
```